Ferris Contracting LLC Business Card Design

I am looking for a creative and unique business card design. We are a commercial construction general contractor. With the name "FERRIS" Contracting, I am hoping to see some neat designs that correlate with the name.

```html
<!DOCTYPE html>
<html lang="en">
<head>
<meta charset="utf-8">
<title>Ferris Contracting LLC – Business Card</title>
<link rel="stylesheet" href="https://fonts.googleapis.com/css2?family=Oswald:wght@400;500;600&family=Roboto+Condensed:ital,wght@0,400;1,600&display=swap">
<style>
  :root {
    --bg: #d8d6d1;
    --card-black: #141414;
    --charcoal: #1e2023;
    --steel: #8d9196;
    --steel-light: #b9bcc0;
    --blue: #1f5b9a;
    --blue-bright: #3b8fd6;
    --blue-deep: #163f6c;
    --white: #ffffff;
    --name-box: #2b2c2e;
  }
  * { margin: 0; padding: 0; box-sizing: border-box; }
  html, body { width: 1200px; height: 776px; overflow: hidden; }
  body { background: var(--bg); position: relative; font-family: "Oswald", sans-serif; }

  .card {
    position: absolute;
    width: 560px;
    height: 361px;
    border-radius: 16px;
    overflow: hidden;
  }

  /* Front */
  .card-front {
    left: 40px; top: 28px;
    background: radial-gradient(ellipse at 45% 40%, #262626 0%, var(--card-black) 70%);
  }
  .brand {
    position: absolute;
    left: 0; right: 0; top: 96px;
    display: flex; align-items: center; justify-content: center; gap: 18px;
  }
  .brand-dot {
    width: 62px; height: 62px; border-radius: 50%;
    background: var(--blue-bright);
  }
  .brand-name {
    color: var(--blue-bright);
    font-weight: 600;
    line-height: 1;
  }
  .brand-name .word-main { display: block; font-size: 84px; letter-spacing: 2px; }
  .brand-name .word-sub { display: block; font-size: 27px; letter-spacing: 9px; margin-top: 4px; }
  .tagline {
    position: absolute; left: 0; right: 0; top: 300px;
    text-align: center;
    color: var(--white);
    font-family: "Roboto Condensed", sans-serif;
    font-size: 21px; letter-spacing: 0.3px;
  }

  /* Back */
  .card-back { left: 600px; top: 395px; background: var(--charcoal); }
  .card-back .backdrop { position: absolute; inset: 0; }
  .name-box {
    position: absolute; left: 292px; top: 50px; width: 268px; height: 86px;
    background: var(--name-box);
    padding: 6px 0 0 22px;
    color: var(--white);
  }
  .person-name { font-size: 38px; font-weight: 500; line-height: 1.1; letter-spacing: 0.5px; }
  .person-role {
    font-family: "Roboto Condensed", sans-serif;
    font-style: italic; font-weight: 600; font-size: 17px;
  }
  .contact {
    position: absolute; left: 303px; top: 146px;
    color: var(--white);
    font-family: "Roboto Condensed", sans-serif;
    font-size: 16.5px; line-height: 21px;
  }
  .contact .address { margin-bottom: 2px; }
  .contact .label { font-weight: 600; display: inline-block; width: 16px; }
  .services {
    position: absolute; left: 190px; top: 298px; width: 340px;
    color: var(--white);
    font-family: "Roboto Condensed", sans-serif;
    font-size: 13.5px; line-height: 18px;
  }
</style>
</head>
<body>

<section class="card card-front" aria-label="Business card front">
  <div class="brand">
    <span class="brand-dot"></span>
    <div class="brand-name">
      <span class="word-main">FERRIS</span>
      <span class="word-sub">CONTRACTING</span>
    </div>
  </div>
  <p class="tagline">INDUSTRIAL &amp; COMMERCIAL SERVICES</p>
</section>

<section class="card card-back" aria-label="Business card back">
  <svg class="backdrop" width="560" height="361" viewBox="0 0 560 361">
    <defs>
      <linearGradient id="steelBand" x1="0" y1="0" x2="1" y2="1">
        <stop offset="0" stop-color="#6d7176"/>
        <stop offset="0.5" stop-color="#a9acb0"/>
        <stop offset="1" stop-color="#5c6065"/>
      </linearGradient>
      <linearGradient id="bluePanel" x1="0" y1="0" x2="1" y2="0">
        <stop offset="0" stop-color="#1a4c82"/>
        <stop offset="1" stop-color="#1f5b9a"/>
      </linearGradient>
    </defs>
    <polygon points="330,0 560,0 560,286 150,286" fill="url(#bluePanel)"/>
    <polygon points="20,361 300,0 322,0 42,361" fill="url(#steelBand)"/>
    <polygon points="0,120 90,0 108,0 0,144" fill="url(#steelBand)"/>
    <polygon points="0,250 110,110 250,250 160,361 140,361 230,250 110,130 0,272" fill="url(#steelBand)" opacity="0.85"/>
    <polygon points="120,361 400,0 414,0 134,361" fill="#3a3d41"/>
    <g role="img" aria-label="Diamond plate texture area">
      <rect x="500" y="0" width="60" height="130" fill="#1d4f86"/>
      <rect x="500" y="286" width="60" height="75" fill="#1d4f86"/>
    </g>
    <rect x="0" y="286" width="560" height="75" fill="#17191b" opacity="0.85"/>
  </svg>

  <div class="name-box">
    <h1 class="person-name">DAN MERCER</h1>
    <p class="person-role">Owner / Project Manager</p>
  </div>

  <div class="contact">
    <p class="address">123 CONTRACTOR'S WAY<br>CITY, STATE 12345</p>
    <p><span class="label">T:</span> (123) 456-7890</p>
    <p><span class="label">E:</span> info@ferriscontracting.com</p>
    <p><span class="label">W:</span> www.ferriscontracting.com</p>
  </div>

  <p class="services">SERVICES: INDUSTRIAL CONSTRUCTION, SITE WORK,<br>DEMOLITION, PROJECT MANAGEMENT</p>
</section>

</body>
</html>
```